ramadan product promo calendar 2021

Ramadan Calender showcase our promotions during the month of ramadan. Please see previous calenders for inspiration. Must be different not the same as previous years!. Please only use greens golds as main colours. Must be double sided. A4 size.

Target Market(s)

Customers

Industry/Entity Type

Retail

Font styles to use
Decorative

Colors
9bcb3c
ffffff
ffc214

Requirements
Must have
• Must only use green and gold. You ca experiment with different shades.
Must have space for timetable. Must show case at 26 product offers. Product offers cannot be too small. Must have our logo. Please see previous years for clarity. Must look professional designed and elegant so customers are willing to keep it on display for the whole month.
Nice to have
• Islamic patterns, Islamic designs.
Should not have
• Any other colour.

```html
<!DOCTYPE html>
<html lang="en">
<head>
<meta charset="utf-8">
<title>Ramadan 2021 Timetable</title>
<link href="https://fonts.googleapis.com/css2?family=Kaushan+Script&family=Roboto:ital,wght@0,400;0,500;0,700;0,900;1,700;1,900&family=Julius+Sans+One&display=swap" rel="stylesheet">
<style>
:root{
  --backdrop:#5f9e45;
  --deep-green:#0c4a27;
  --stripe-green:#0b9a3c;
  --light-green:#b9e35a;
  --pale-green:#dff59a;
  --gold:#f0b417;
  --yellow:#fff34a;
  --title-yellow:#f5f07a;
  --white:#ffffff;
  --orange:#e67a1a;
  --lantern:#e8913a;
}
*{margin:0;padding:0;box-sizing:border-box}
html,body{width:955px;height:1200px;overflow:hidden;background:var(--backdrop)}
.poster{position:absolute;left:107px;top:75px;width:741px;height:1049px;background:var(--deep-green);overflow:hidden;box-shadow:0 8px 30px rgba(0,0,0,.35);font-family:"Roboto",Arial,sans-serif}
.header-sky{position:absolute;left:0;top:0;width:741px;height:312px;background:radial-gradient(circle at 85% 40%,#8fd13a 0,transparent 30%),linear-gradient(100deg,var(--light-green),var(--pale-green) 40%,var(--light-green) 75%,#a6d94a)}
.arch{position:absolute;left:0;top:0}
.lantern{position:absolute;background:linear-gradient(90deg,#b85d17,var(--lantern) 40%,#f7b56a 60%,#b85d17);border-radius:6px 6px 3px 3px}
.title{position:absolute;left:0;top:0;width:741px;height:312px}
.title-script{position:absolute;left:214px;top:172px;font-family:"Kaushan Script",cursive;font-size:72px;color:var(--title-yellow);line-height:1}
.title-year{position:absolute;left:428px;top:160px;font-family:"Kaushan Script",cursive;font-size:38px;color:var(--title-yellow);line-height:1}
.title-sub{position:absolute;left:312px;top:246px;font-family:"Julius Sans One",sans-serif;font-size:25px;letter-spacing:4px;color:var(--white);line-height:1}
.timetable{position:absolute;left:13px;top:315px;width:489px}
.row{display:grid;grid-template-columns:47px 54px 66px 54px 57px 63px 60px 50px;padding-left:36px;height:22.1px;align-items:center;font-size:12.5px;color:var(--white)}
.row.head{height:22px;font-weight:900;font-style:italic;font-size:13px;background:linear-gradient(90deg,transparent,var(--stripe-green) 6%)}
.row:nth-child(odd):not(.head){background:linear-gradient(90deg,transparent,var(--stripe-green) 8%)}
.row span:nth-child(1){font-weight:900;font-style:italic}
.row span:nth-child(2),.row span:nth-child(4),.row span:nth-child(6),.row span:nth-child(8){color:var(--yellow)}
.row.head span:nth-child(3){font-style:normal;font-weight:400}
.row span:nth-child(3){font-weight:500}
.offers{position:absolute;left:503px;top:317px;width:208px;height:688px;border:3px solid var(--yellow);border-radius:28px;overflow:hidden;box-shadow:10px 6px 0 #093d1f}
.brand{height:60px;background:var(--orange);text-align:center;color:var(--deep-green);font-weight:700;line-height:1}
.brand-name{display:block;font-size:30px;letter-spacing:14px;padding-top:10px;padding-left:14px}
.brand-sub{display:flex;align-items:center;justify-content:center;gap:5px;font-size:8px;letter-spacing:4px;margin-top:4px}
.brand-sub::before,.brand-sub::after{content:"";width:34px;height:1px;background:var(--deep-green)}
.offer{position:absolute;left:9px;width:178px;height:69px;border:2px solid var(--yellow);border-radius:14px;display:flex;align-items:center;padding-left:13px;gap:17px}
.offer-photo{width:48px;height:48px;background:var(--white);display:flex;align-items:center;justify-content:center;flex:none}
.offer-photo i{display:block;width:28px;height:40px;background:linear-gradient(135deg,#d8432a,#f05a3a);border-radius:3px}
.offer-text{color:var(--yellow);font-weight:700;line-height:1.15;white-space:nowrap}
.offer-brand{font-size:12.5px}
.offer-item{font-size:12px}
.offer-price{font-size:25px;font-weight:700;line-height:1}
.footer-pattern{position:absolute;left:0;top:1005px;width:741px;height:44px;background:linear-gradient(180deg,var(--deep-green),#0f5a2e)}
</style>
</head>
<body>
<div class="poster">
  <div class="header-sky" role="img" aria-label="Soft green bokeh background with golden Islamic geometric pattern"></div>
  <svg class="arch" width="741" height="330" viewBox="0 0 741 330">
    <path d="M-5,330 L-5,310 L95,310 Q108,272 150,268 L166,268 Q181,265 181,242 L181,205 Q186,135 280,92 Q343,62 370,20 Q397,62 460,92 Q554,135 559,205 L559,242 Q559,265 574,268 L590,268 Q632,272 646,310 L746,310 L746,330 Z" fill="var(--deep-green)" stroke="var(--white)" stroke-width="12"/>
    <path d="M-5,330 L-5,310 L95,310 Q108,272 150,268 L166,268 Q181,265 181,242 L181,205 Q186,135 280,92 Q343,62 370,20 Q397,62 460,92 Q554,135 559,205 L559,242 Q559,265 574,268 L590,268 Q632,272 646,310 L746,310 L746,330 Z" fill="var(--deep-green)" stroke="var(--gold)" stroke-width="8"/>
  </svg>
  <div class="lantern" role="img" aria-label="Hanging golden lantern" style="left:20px;top:115px;width:65px;height:135px"></div>
  <div class="lantern" role="img" aria-label="Hanging golden lantern" style="left:100px;top:70px;width:45px;height:85px"></div>
  <div class="lantern" role="img" aria-label="Hanging golden lantern" style="left:590px;top:70px;width:45px;height:85px"></div>
  <div class="lantern" role="img" aria-label="Hanging golden lantern" style="left:645px;top:115px;width:65px;height:135px"></div>
  <div class="title">
    <span class="title-year">2021</span>
    <span class="title-script">Ramadan</span>
    <span class="title-sub">TIMETABLE</span>
  </div>

  <div class="timetable">
    <div class="row head"><span>Fast</span><span>Date</span><span>Day</span><span>Sehri</span><span>Zhur</span><span>Asr</span><span>Iftar</span><span>Isha</span></div>
    <div class="row"><span>1</span><span>Apr 13</span><span>Tue</span><span>4:34</span><span>1:06</span><span>16:48</span><span>19:57</span><span>21:12</span></div>
    <div class="row"><span>2</span><span>Apr 14</span><span>Wed</span><span>4:34</span><span>1:06</span><span>16:48</span><span>19:57</span><span>21:12</span></div>
    <div class="row"><span>3</span><span>Apr 15</span><span>Thu</span><span>4:34</span><span>1:06</span><span>16:48</span><span>19:57</span><span>21:12</span></div>
    <div class="row"><span>4</span><span>Apr 15</span><span>Thu</span><span>4:34</span><span>1:06</span><span>16:48</span><span>19:57</span><span>21:12</span></div>
    <div class="row"><span>5</span><span>Apr 15</span><span>Thu</span><span>4:34</span><span>1:06</span><span>16:48</span><span>19:57</span><span>21:12</span></div>
    <div class="row"><span>6</span><span>Apr 15</span><span>Thu</span><span>4:34</span><span>1:06</span><span>16:48</span><span>19:57</span><span>21:12</span></div>
    <div class="row"><span>7</span><span>Apr 15</span><span>Thu</span><span>4:34</span><span>1:06</span><span>16:48</span><span>19:57</span><span>21:12</span></div>
    <div class="row"><span>8</span><span>Apr 15</span><span>Thu</span><span>4:34</span><span>1:06</span><span>16:48</span><span>19:57</span><span>21:12</span></div>
    <div class="row"><span>9</span><span>Apr 15</span><span>Thu</span><span>4:34</span><span>1:06</span><span>16:48</span><span>19:57</span><span>21:12</span></div>
    <div class="row"><span>10</span><span>Apr 15</span><span>Thu</span><span>4:34</span><span>1:06</span><span>16:48</span><span>19:57</span><span>21:12</span></div>
    <div class="row"><span>11</span><span>Apr 15</span><span>Thu</span><span>4:34</span><span>1:06</span><span>16:48</span><span>19:57</span><span>21:12</span></div>
    <div class="row"><span>12</span><span>Apr 15</span><span>Thu</span><span>4:34</span><span>1:06</span><span>16:48</span><span>19:57</span><span>21:12</span></div>
    <div class="row"><span>13</span><span>Apr 15</span><span>Thu</span><span>4:34</span><span>1:06</span><span>16:48</span><span>19:57</span><span>21:12</span></div>
    <div class="row"><span>14</span><span>Apr 15</span><span>Thu</span><span>4:34</span><span>1:06</span><span>16:48</span><span>19:57</span><span>21:12</span></div>
    <div class="row"><span>15</span><span>Apr 15</span><span>Thu</span><span>4:34</span><span>1:06</span><span>16:48</span><span>19:57</span><span>21:12</span></div>
    <div class="row"><span>16</span><span>Apr 15</span><span>Thu</span><span>4:34</span><span>1:06</span><span>16:48</span><span>19:57</span><span>21:12</span></div>
    <div class="row"><span>17</span><span>Apr 15</span><span>Thu</span><span>4:34</span><span>1:06</span><span>16:48</span><span>19:57</span><span>21:12</span></div>
    <div class="row"><span>18</span><span>Apr 15</span><span>Thu</span><span>4:34</span><span>1:06</span><span>16:48</span><span>19:57</span><span>21:12</span></div>
    <div class="row"><span>19</span><span>Apr 15</span><span>Thu</span><span>4:34</span><span>1:06</span><span>16:48</span><span>19:57</span><span>21:12</span></div>
    <div class="row"><span>20</span><span>Apr 15</span><span>Thu</span><span>4:34</span><span>1:06</span><span>16:48</span><span>19:57</span><span>21:12</span></div>
    <div class="row"><span>21</span><span>Apr 15</span><span>Thu</span><span>4:34</span><span>1:06</span><span>16:48</span><span>19:57</span><span>21:12</span></div>
    <div class="row"><span>22</span><span>Apr 15</span><span>Thu</span><span>4:34</span><span>1:06</span><span>16:48</span><span>19:57</span><span>21:12</span></div>
    <div class="row"><span>23</span><span>Apr 15</span><span>Thu</span><span>4:34</span><span>1:06</span><span>16:48</span><span>19:57</span><span>21:12</span></div>
    <div class="row"><span>24</span><span>Apr 15</span><span>Thu</span><span>4:34</span><span>1:06</span><span>16:48</span><span>19:57</span><span>21:12</span></div>
    <div class="row"><span>25</span><span>Apr 15</span><span>Thu</span><span>4:34</span><span>1:06</span><span>16:48</span><span>19:57</span><span>21:12</span></div>
    <div class="row"><span>26</span><span>Apr 15</span><span>Thu</span><span>4:34</span><span>1:06</span><span>16:48</span><span>19:57</span><span>21:12</span></div>
    <div class="row"><span>27</span><span>Apr 15</span><span>Thu</span><span>4:34</span><span>1:06</span><span>16:48</span><span>19:57</span><span>21:12</span></div>
    <div class="row"><span>28</span><span>Apr 15</span><span>Thu</span><span>4:34</span><span>1:06</span><span>16:48</span><span>19:57</span><span>21:12</span></div>
    <div class="row"><span>29</span><span>Apr 15</span><span>Thu</span><span>4:34</span><span>1:06</span><span>16:48</span><span>19:57</span><span>21:12</span></div>
    <div class="row"><span>30</span><span>Apr 15</span><span>Thu</span><span>4:34</span><span>1:06</span><span>16:48</span><span>19:57</span><span>21:12</span></div>
  </div>

  <div class="offers">
    <div class="brand"><span class="brand-name">NOOR</span><span class="brand-sub">GROCERS</span></div>
    <div class="offer" style="top:85px"><div class="offer-photo" role="img" aria-label="Rice bag product photo"><i></i></div><div class="offer-text"><div class="offer-brand">NOOR</div><div class="offer-item">BASMATI 20KG</div><div class="offer-price">$ 26.99</div></div></div>
    <div class="offer" style="top:168px"><div class="offer-photo" role="img" aria-label="Rice bag product photo"><i></i></div><div class="offer-text"><div class="offer-brand">NOOR</div><div class="offer-item">BASMATI 20KG</div><div class="offer-price">$ 26.99</div></div></div>
    <div class="offer" style="top:252px"><div class="offer-photo" role="img" aria-label="Rice bag product photo"><i></i></div><div class="offer-text"><div class="offer-brand">NOOR</div><div class="offer-item">BASMATI 20KG</div><div class="offer-price">$ 26.99</div></div></div>
    <div class="offer" style="top:335px"><div class="offer-photo" role="img" aria-label="Rice bag product photo"><i></i></div><div class="offer-text"><div class="offer-brand">NOOR</div><div class="offer-item">BASMATI 20KG</div><div class="offer-price">$ 26.99</div></div></div>
    <div class="offer" style="top:419px"><div class="offer-photo" role="img" aria-label="Rice bag product photo"><i></i></div><div class="offer-text"><div class="offer-brand">NOOR</div><div class="offer-item">BASMATI 20KG</div><div class="offer-price">$ 26.99</div></div></div>
    <div class="offer" style="top:502px"><div class="offer-photo" role="img" aria-label="Rice bag product photo"><i></i></div><div class="offer-text"><div class="offer-brand">NOOR</div><div class="offer-item">BASMATI 20KG</div><div class="offer-price">$ 26.99</div></div></div>
    <div class="offer" style="top:586px"><div class="offer-photo" role="img" aria-label="Rice bag product photo"><i></i></div><div class="offer-text"><div class="offer-brand">NOOR</div><div class="offer-item">BASMATI 20KG</div><div class="offer-price">$ 26.99</div></div></div>
  </div>

  <div class="footer-pattern" role="img" aria-label="Golden Islamic geometric border pattern"></div>
</div>
</body>
</html>
```